Business Card Design Project

We have 2 businesses which help each other.

Maplewick Care (providing nurses to hospitals/nursing homes etc)

and

Maplewick HR (providing nurses to our maplewick care business - but also providing workers for farms, restaurants meatworks etc)

We would like 2 separate business cards - but similar design and feel

Target Market(s)

Managers of nursing homes, hospitals, farms, meatworks, restauants

Industry/Entity Type

Business

Requirements
Must have
• both logos
https://www.filecrate.example/s/9q2m7t4kzrx8vbn/MaplewickHR-Logo-Horizontal.ai
https://www.filecrate.example/s/kp57wx2nb8y4q1h/73918_215607_88264_sourcefile.ai

You may edit the layout of Maplewick HR logo

Name
position
mobile
Phone
name@maplewickhr.com.au
mapelwickhr.com.au

Name
position
mobile
phone
name@maplewickcare.net.au
maplewickcare.net.au

```html
<!DOCTYPE html>
<html lang="en">
<head>
<meta charset="utf-8">
<title>Maplewick Business Cards</title>
<link rel="stylesheet" href="https://fonts.googleapis.com/css2?family=Open+Sans:wght@400;600;700&display=swap">
<style>
  :root {
    --backdrop: #1b1b1b;
    --white: #ffffff;
    --blue-deep: #0e4f9e;
    --blue-mid: #1a63b8;
    --blue-light: #3b86d4;
    --brand-navy: #2e3192;
    --brand-sky: #1f8fd8;
    --silver: #c9ccd1;
    --silver-dark: #8f949b;
    --globe: #a9bfe6;
  }
  * { margin: 0; padding: 0; box-sizing: border-box; }
  html, body { width: 1200px; height: 900px; overflow: hidden; }
  body {
    background: var(--backdrop);
    font-family: "Open Sans", sans-serif;
    position: relative;
  }
  .card {
    position: absolute;
    border-radius: 24px;
    overflow: hidden;
    color: var(--white);
  }
  .card--hr-front   { left: 33px;  top: 78px;  width: 550px; height: 355px; }
  .card--hr-back    { left: 609px; top: 78px;  width: 554px; height: 357px; }
  .card--care-front { left: 28px;  top: 483px; width: 552px; height: 355px; }
  .card--care-back  { left: 610px; top: 485px; width: 557px; height: 358px; }

  .card-back-fill {
    position: absolute; inset: 0;
    background: linear-gradient(100deg, var(--blue-light) 0%, var(--blue-mid) 45%, var(--blue-deep) 100%);
  }
  .front-shape { position: absolute; inset: 0; width: 100%; height: 100%; }

  .brand-mark {
    position: absolute;
    font-weight: 700;
    letter-spacing: -0.5px;
    white-space: nowrap;
  }
  .brand-dot {
    position: absolute;
    border-radius: 50%;
    background: radial-gradient(circle at 40% 35%, #ffffff 0%, #c6d3e6 60%, #9fb1cc 100%);
  }

  .holder-name { position: absolute; font-size: 24px; font-weight: 400; }
  .holder-role { position: absolute; font-size: 15px; }
  .divider {
    position: absolute; width: 2px; height: 68px;
    background: linear-gradient(180deg, transparent, var(--silver), transparent);
  }
  .contact-list {
    position: absolute; list-style: none;
    font-size: 15px; line-height: 19.5px;
  }

  .globe-disc {
    position: absolute; border-radius: 50%;
    background: radial-gradient(circle at 45% 40%, #c8d7f2 0%, var(--globe) 50%, #6f93cf 100%);
  }
  .back-url { position: absolute; font-size: 14px; }
  .back-blurb {
    position: absolute; left: 0; right: 0;
    text-align: center; font-size: 14px; line-height: 20px;
  }
</style>
</head>
<body>

  <!-- Maplewick HR front -->
  <section class="card card--hr-front">
    <svg class="front-shape" viewBox="0 0 550 355" preserveAspectRatio="none" aria-hidden="true">
      <defs>
        <linearGradient id="hrBlue" x1="0" y1="0" x2="1" y2="0">
          <stop offset="0" stop-color="#2a78cc"/><stop offset="1" stop-color="#0e4f9e"/>
        </linearGradient>
        <linearGradient id="hrSilver" x1="0" y1="0" x2="1" y2="0">
          <stop offset="0" stop-color="#8f949b"/><stop offset="0.5" stop-color="#e8eaed"/><stop offset="1" stop-color="#9aa0a7"/>
        </linearGradient>
      </defs>
      <rect width="550" height="355" fill="#ffffff"/>
      <path d="M0,168 C160,232 360,250 550,140 L550,355 L0,355 Z" fill="url(#hrSilver)"/>
      <path d="M0,180 C170,244 370,258 550,162 L550,355 L0,355 Z" fill="url(#hrBlue)"/>
      <path d="M0,168 C150,222 330,236 500,168" fill="none" stroke="#1a63b8" stroke-width="3"/>
    </svg>
    <span class="brand-dot" style="left:95px; top:45px; width:80px; height:80px;"></span>
    <span class="brand-mark" style="left:190px; top:60px; font-size:40px; color:var(--blue-deep);">maplewickHR</span>
    <span class="holder-name" style="left:31px; top:255px;">Your Name</span>
    <span class="holder-role" style="left:110px; top:285px;">Position</span>
    <span class="divider" style="left:264px; top:262px;"></span>
    <ul class="contact-list" style="left:305px; top:254px;">
      <li>M: 000 000 0000</li>
      <li>P : 000 0000</li>
      <li>E :name@maplewickhr.com.au</li>
      <li>I : www.maplewickhr.com.au</li>
    </ul>
  </section>

  <!-- Maplewick HR back -->
  <section class="card card--hr-back">
    <div class="card-back-fill"></div>
    <div class="globe-disc" role="img" aria-label="Globe illustration area" style="left:-40px; top:-30px; width:290px; height:290px;"></div>
    <span class="brand-mark" style="left:257px; top:103px; font-size:40px; color:var(--white);">maplewickHR</span>
    <span class="back-url" style="left:299px; top:151px;">www.maplewickhr.com.au</span>
    <p class="back-blurb" style="top:299px;">Providing nurses to our maplewick care business-but also providing<br>workers for farms, restaurants meatworks etc</p>
  </section>

  <!-- Maplewick Care front -->
  <section class="card card--care-front">
    <svg class="front-shape" viewBox="0 0 552 355" preserveAspectRatio="none" aria-hidden="true">
      <defs>
        <linearGradient id="careBlue" x1="0" y1="0" x2="1" y2="0">
          <stop offset="0" stop-color="#2a78cc"/><stop offset="1" stop-color="#0e4f9e"/>
        </linearGradient>
        <linearGradient id="careSilver" x1="0" y1="0" x2="1" y2="0">
          <stop offset="0" stop-color="#8f949b"/><stop offset="0.5" stop-color="#e8eaed"/><stop offset="1" stop-color="#9aa0a7"/>
        </linearGradient>
      </defs>
      <rect width="552" height="355" fill="#ffffff"/>
      <path d="M0,168 C160,232 360,250 552,140 L552,355 L0,355 Z" fill="url(#careSilver)"/>
      <path d="M0,180 C170,244 370,258 552,162 L552,355 L0,355 Z" fill="url(#careBlue)"/>
      <path d="M0,168 C150,222 330,236 500,168" fill="none" stroke="#1a63b8" stroke-width="3"/>
    </svg>
    <span class="brand-mark" style="left:82px; top:80px; font-size:50px; color:var(--brand-navy);">maplewickcare</span>
    <span class="holder-name" style="left:48px; top:255px;">Your Name</span>
    <span class="holder-role" style="left:127px; top:285px;">Position</span>
    <span class="divider" style="left:240px; top:262px;"></span>
    <ul class="contact-list" style="left:282px; top:254px;">
      <li>M: 000 000 0000</li>
      <li>P : 000 0000</li>
      <li>E :name@maplewickcare.net.au</li>
      <li>I : www.maplewickcare.net.au</li>
    </ul>
  </section>

  <!-- Maplewick Care back -->
  <section class="card card--care-back">
    <div class="card-back-fill"></div>
    <span class="brand-mark" style="left:205px; top:96px; font-size:36px; color:var(--white);">maplewickcare</span>
    <p class="back-blurb" style="top:292px;">providing nurses to hospitals/ nursing homes etc<br>www.maplewickcare.net.au</p>
  </section>

</body>
</html>
```